Surgical Sales Presentation Folder

Presentation folder; three panel; custom cutouts; Six 8.5 x 11 full color sales sheets to be bound into presentation folder; 5 full color sales sheets, stepped, longest being 8.5 x 11.
We are Brantley Surgical Group and we are a surgical company that supports physicians who wish to become surgeons. Our clients are Physicians. As such, the design needs to be very professional.
I have included a list of photos and a letter describing what we like about each photo. I have included the verbiage with page identifiers. If this makes scene, please feel free to add photos to the inside of the folder or I can provide you with examples that we think are similar to what we are looking for.
Updates
Target Market(s)
Doctors who want to be surgeons.
Industry/Entity Type
Sales
Requirements
Must have
- Presentation folder; three panel; custom cutouts; Six 8.5 x 11 full color sales sheets to be bound into presentation folder; 5 full color sales sheets, stepped, longest being 8.5 x 11.

```html
<!DOCTYPE html>
<html lang="en">
<head>
<meta charset="utf-8">
<title>Career Satisfaction</title>
<link rel="stylesheet" href="https://fonts.googleapis.com/css2?family=Montserrat:wght@600;700;800&family=Crimson+Text:ital@0;1&display=swap">
<style>
  :root {
    --blue: #0a8fc4;
    --red: #c0392b;
    --ink: #1e1e1e;
    --white: #ffffff;
    --sketch-light: #fbfbfb;
    --sketch-mid: #ececec;
  }
  * { margin: 0; padding: 0; box-sizing: border-box; }
  html, body { width: 927px; height: 1200px; overflow: hidden; background: var(--white); }
  .page { position: relative; width: 927px; height: 1200px; overflow: hidden; background: var(--white); }

  .quote-band { position: absolute; left: 0; top: 0; width: 927px; height: 434px; background: var(--blue); }
  .quote-mark {
    position: absolute; color: var(--white);
    font-family: "Montserrat", sans-serif; font-weight: 800;
    font-size: 230px; line-height: 1;
  }
  .quote-mark--open { left: 86px; top: 20px; }
  .quote-mark--close { left: 764px; top: 205px; }
  .quote-text {
    position: absolute; left: 232px; top: 48px; width: 640px;
    color: var(--white); font-family: "Montserrat", sans-serif; font-weight: 600;
    font-size: 30px; line-height: 40px; text-align: justify; letter-spacing: -0.2px;
  }
  .quote-author {
    position: absolute; left: 232px; top: 258px;
    color: var(--white); font-family: "Crimson Text", serif; font-style: italic;
    font-size: 31px;
  }

  .sketch-caduceus {
    position: absolute; left: 344px; top: 434px; width: 583px; height: 766px;
    background: radial-gradient(ellipse at 55% 40%, var(--sketch-mid), var(--sketch-light) 70%, var(--white));
  }

  .title-block { position: absolute; left: 54px; top: 434px; width: 290px; height: 166px; background: var(--red); }
  .title {
    position: absolute; left: 52px; top: 496px;
    color: var(--white); font-family: "Montserrat", sans-serif; font-weight: 700;
    font-size: 38px; line-height: 42px;
  }

  .side-bar { position: absolute; left: 0; top: 630px; width: 54px; height: 168px; background: var(--blue); }

  .column {
    position: absolute; top: 626px; width: 224px;
    font-family: "Crimson Text", serif; font-size: 17.5px; line-height: 21.7px;
    color: var(--ink); text-align: justify; hyphens: auto;
  }
  .column--one { left: 91px; }
  .column--two { left: 370px; }
  .column--three { left: 648px; }
  .factor-list { list-style: none; margin-top: 21.7px; color: var(--blue); font-style: italic; text-align: left; }
  .factor-list li { position: relative; padding-left: 18px; }
  .factor-list li::before { content: "•"; position: absolute; left: 0; font-style: normal; }

  .page-number {
    position: absolute; left: 872px; top: 1094px; width: 55px; height: 106px;
    background: var(--blue); color: var(--white);
    font-family: "Montserrat", sans-serif; font-size: 18px;
    display: flex; align-items: flex-end; justify-content: center; padding-bottom: 12px;
  }
</style>
</head>
<body>
<div class="page">
  <section class="quote-band">
    <span class="quote-mark quote-mark--open">&ldquo;</span>
    <p class="quote-text">In the mid-20th Century, physicians were the pillars of any community. If you were smart, sincere and ambitious, there was nothing nobler or more rewarding that you could aspire to become.</p>
    <p class="quote-author">- Dr. Martin Ellery</p>
    <span class="quote-mark quote-mark--close">&rdquo;</span>
  </section>

  <div class="sketch-caduceus" role="img" aria-label="Faint pencil sketch of a winged staff entwined with serpents"></div>

  <div class="title-block"></div>
  <h1 class="title">Career<br>Satisfaction</h1>
  <div class="side-bar"></div>

  <div class="column column--one">
    <p>What makes a physician happy with their career choice? According to a study conducted at Eastbrook State University, factors that make a significant positive impact on a physician&rsquo;s career satisfaction are:</p>
    <ul class="factor-list">
      <li>The ability to provide quality care</li>
      <li>The ability to spend time with their patients</li>
      <li>Income &amp; Financial Incentives</li>
    </ul>
  </div>

  <div class="column column--two">
    <p>In other words, when a physician or a surgeon, can make a significant difference in the lives of his patients, providing quality care, while meeting the financial needs of his family, he experiences a far greater degree of career satisfaction. Through the years, the high quality of patient care provided by physicians has remained consistent. However, based the needs of their medical practice many</p>
  </div>

  <div class="column column--three">
    <p>physicians find themselves needing to spend less time with a greater number of patients. They also commit a larger percentage of their income to the maintenance of their practice.</p>
    <p>What are the results of these trends? A National Business Ledger survey of 12,000 physicians found only 6% described their morale as positive.</p>
  </div>

  <div class="page-number">1</div>
</div>
</body>
</html>
```